Flyer-Design für Naturkosmetik und Wellness
Zielgruppe
Naturkosmetik und Wellness
Aufgabenstellung
Das Design soll schlicht sein , aber nicht unscheinbar wirken. Ich möchte die Flyer gerne als Postkarte vorne und hinten gestaltet.
Vorderseite : Mein Name im gleichen Design , wie bei meinen Visitenkarten.Text:Kosmetik und Entspannung im Einklang mit der Natur .
Rückseite : Termine nach Vereinbarung Mo 16.00 h- 19.00h , Mi und Do 15.00h - 19.00h und Fr 14.00h - 18.00h

```html
<!DOCTYPE html>
<html lang="de">
<head>
<meta charset="utf-8">
<title>Postkarte – Petra Wolken</title>
<link rel="stylesheet" href="https://fonts.googleapis.com/css2?family=Quicksand:wght@400;500&family=Open+Sans:wght@400;600&display=swap">
<style>
  :root {
    --page: #ecebea;
    --card-edge: #d4d2cf;
    --paper: #ffffff;
    --front-fill: #e8e6e3;
    --band-dark: #7d7a77;
    --band-light: #a9a6a2;
    --ink: #6d6a67;
    --ink-soft: #9a9692;
    --line: #c9c6c2;
    --white: #ffffff;
  }
  * { margin: 0; padding: 0; box-sizing: border-box; }
  html, body { width: 675px; height: 1200px; overflow: hidden; }
  body { background: var(--page); font-family: "Open Sans", sans-serif; color: var(--ink); position: relative; }

  .postcard {
    position: absolute; left: 40px; width: 595px; height: 420px;
    background: var(--card-edge); padding: 12px;
    box-shadow: 0 2px 6px rgba(0,0,0,.08);
  }
  .postcard--front { top: 150px; }
  .postcard--back { top: 640px; }
  .postcard__inner { position: relative; width: 100%; height: 100%; background: var(--paper); overflow: hidden; }

  /* Front */
  .front { background: var(--front-fill); }
  .front__photo {
    position: absolute; left: 0; top: 0; width: 100%; height: 132px;
    background: linear-gradient(160deg, var(--band-dark) 0%, var(--band-light) 55%, #8f8b87 100%);
  }
  .front__headline {
    position: absolute; left: 0; top: 40px; width: 100%; text-align: center;
    font-family: "Quicksand", sans-serif; font-weight: 500; font-size: 21px; line-height: 1.3;
    color: var(--white); letter-spacing: .3px;
  }
  .front__name {
    position: absolute; left: 0; top: 200px; width: 100%; text-align: center;
    font-family: "Quicksand", sans-serif; font-weight: 400; font-size: 40px; line-height: 1.2;
    color: var(--ink); letter-spacing: 1px;
  }
  .front__web { position: absolute; left: 0; bottom: 28px; width: 100%; text-align: center; font-size: 12px; color: var(--ink); }

  /* Back */
  .back__info { position: absolute; left: 30px; top: 26px; width: 250px; }
  .back__name {
    font-family: "Quicksand", sans-serif; font-weight: 400; font-size: 22px; line-height: 1.2;
    color: var(--ink); letter-spacing: .5px;
  }
  .hours { margin-top: 40px; font-size: 11px; }
  .hours__title { margin-bottom: 8px; }
  .hours__list { list-style: none; padding-left: 6px; }
  .hours__list li { display: flex; align-items: center; gap: 7px; margin-bottom: 4px; }
  .bullet { width: 5px; height: 5px; background: var(--ink-soft); flex: none; }
  .contact { position: absolute; left: 30px; bottom: 28px; font-size: 9px; color: var(--ink-soft); }
  .contact__name { font-size: 10px; font-weight: 600; color: var(--ink); margin-bottom: 4px; }
  .contact__row { display: flex; align-items: center; gap: 6px; margin-bottom: 2px; }

  .back__divider { position: absolute; left: 300px; top: 30px; bottom: 40px; width: 1px; background: var(--line); }
  .stamp { position: absolute; right: 30px; top: 26px; width: 60px; height: 72px; border: 1px solid var(--line); }
  .address-lines { position: absolute; left: 320px; right: 30px; top: 126px; }
  .address-lines span { display: block; height: 1px; background: var(--line); margin-bottom: 30px; }
  .back__web { position: absolute; right: 30px; bottom: 22px; font-size: 10px; color: var(--ink); }
</style>
</head>
<body>

<section class="postcard postcard--front">
  <div class="postcard__inner front">
    <div class="front__photo" role="img" aria-label="Foto: gerollte Frotteehandtücher in Grautönen"></div>
    <p class="front__headline">Kosmetik und Entspannung im<br>Einklang mit der Natur</p>
    <p class="front__name">Petra Wolken</p>
    <p class="front__web">www.ruhezeit-atelier.de</p>
  </div>
</section>

<section class="postcard postcard--back">
  <div class="postcard__inner back">
    <div class="back__info">
      <p class="back__name">Petra Wolken</p>
      <div class="hours">
        <p class="hours__title">Termine nach Vereinbarung</p>
        <ul class="hours__list">
          <li><span class="bullet"></span>Mo 16.00h - 19.00h</li>
          <li><span class="bullet"></span>Mi und Do 15.00h - 19.00h</li>
          <li><span class="bullet"></span>Fr 14.00h - 18.00h</li>
        </ul>
      </div>
    </div>
    <div class="contact">
      <p class="contact__name">Petra Wolken</p>
      <p class="contact__row"><span class="bullet"></span>Lindenweg 12, 73000 Talheim</p>
      <p class="contact__row"><span class="bullet"></span>petra@ruhezeit-atelier.de <span class="bullet"></span>015100000000</p>
    </div>
    <div class="back__divider"></div>
    <div class="stamp"></div>
    <div class="address-lines"><span></span><span></span><span></span><span></span><span></span><span></span></div>
    <p class="back__web">www.ruhezeit-atelier.de</p>
  </div>
</section>

</body>
</html>
```